VelloPath Business Card

Our company is called VelloPath and we are based in Tel Aviv, Israel. We create innovative and exciting methods for getting people on the web engaged with content. We need a cool yet professional business card that will represent our management level employees. keep in mind this is a start up company with a young atmosphere. You can be inspired by our logo (file attached, make sure you have the right font "Ubuntu-Condensed") Use the colors that are used in the logo and create a colourful and professional business card.

```html
<!DOCTYPE html>
<html lang="en">
<head>
<meta charset="utf-8">
<title>VelloPath Business Card</title>
<link rel="stylesheet" href="https://fonts.googleapis.com/css2?family=Ubuntu+Condensed&display=swap">
<style>
  :root {
    --backdrop: #e4e4e4;
    --card: #f7f7f7;
    --ink: #1e1e1e;
    --brand-blue: #1e88d0;
    --pink: #f0449a;
    --purple: #9b4fd1;
    --blue: #3aa6e6;
    --green: #6cc24a;
    --yellow: #f7c531;
    --orange: #f7934c;
  }
  * { box-sizing: border-box; margin: 0; padding: 0; }
  html, body {
    width: 1200px; height: 761px; overflow: hidden;
    background: var(--backdrop);
    font-family: "Ubuntu Condensed", "Arial Narrow", sans-serif;
    color: var(--ink);
  }
  .sheet {
    width: 1200px; height: 761px;
    display: flex; align-items: center; justify-content: center; gap: 50px;
  }
  .card {
    position: relative;
    width: 540px; height: 310px;
    border-radius: 26px;
    overflow: hidden;
    background: var(--card);
    box-shadow: 0 6px 18px rgba(0,0,0,0.18);
  }
  .card__frame {
    position: absolute; inset: 0;
    background:
      linear-gradient(90deg, var(--orange), var(--pink), var(--purple), var(--blue), var(--green), var(--yellow), var(--orange));
    opacity: 0.55;
  }
  .card__field {
    position: absolute; inset: 34px;
    background: var(--card);
    border-radius: 10px;
    box-shadow: 0 0 14px 10px var(--card);
  }
  .brand {
    position: absolute;
    display: flex; align-items: center;
    color: var(--brand-blue);
    font-weight: 400;
  }
  .brand__dot {
    border-radius: 50%;
    background: var(--brand-blue);
  }
  .card--front .brand {
    left: 0; right: 0; top: 118px;
    justify-content: center; gap: 18px;
    font-size: 72px;
  }
  .card--front .brand__dot { width: 46px; height: 46px; }
  .card--back .brand {
    right: 56px; top: 52px; gap: 10px;
    font-size: 28px;
  }
  .card--back .brand__dot { width: 20px; height: 20px; }
  .contact {
    position: absolute; left: 60px; top: 150px;
    font-size: 19px; line-height: 1.15;
  }
  .contact__role { font-size: 22px; }
  .address {
    position: absolute; right: 56px; bottom: 54px;
    font-size: 14px;
  }
</style>
</head>
<body>
<main class="sheet">
  <section class="card card--back">
    <div class="card__frame" role="img" aria-label="Border of colourful radiating bursts in pink, purple, blue, green, yellow and orange"></div>
    <div class="card__field"></div>
    <div class="brand"><span class="brand__dot"></span><span class="brand__name">VelloPath</span></div>
    <div class="contact">
      <p class="contact__role">Director</p>
      <p>054-318-2760</p>
      <p>lead@postbox.net</p>
      <p>lead@vellopath.com</p>
      <p>www.vellopath.com</p>
    </div>
    <p class="address">12 Harbor Lane, Tel Aviv, Israel</p>
  </section>

  <section class="card card--front">
    <div class="card__frame" role="img" aria-label="Border of colourful radiating bursts in pink, purple, blue, green, yellow and orange"></div>
    <div class="card__field"></div>
    <div class="brand"><span class="brand__dot"></span><span class="brand__name">VelloPath</span></div>
  </section>
</main>
</body>
</html>
```